この度はまことにありがとうございます。
広告代理店です。

のぼりデザインのアイデアを頂戴できればと思っております。

入れる文字は下記になります。
梅 の さ と ・ ひ な た べ

ご不明な点などございましたらお気兼ねなくご連絡ください。
何卒、宜しくお願い申し上げます。
サイズの記載がございませんでした。

1800mm縦
600mmよこ

ロゴを縦組みいただいてもかまいません。

何卒、よろしくお願いします。
皆様のご提案に心より感謝申し上げます。

追記
目的をあらためてお知らせします。

このロゴだと背景色が白になりがちです。
しかしながらのぼりを外で使用する場合、背景に色を使わないと目立たないように感じます。

ロゴのイメージを崩さず少し目立つ(目立ちすぎなくて結構です。)のぼりが作れるかを
ご提案いただきたいのが今回の趣旨でございます。

もう1点は洋食っぽい?欧米風?の雰囲気といいますかおしゃれな感じを希望しています。
おしゃれさはかなりのポイントです。

結果的に背景白になるかもですが、、、。
背景が白がNGというわけではなくポイントでどう色を使うかです。

何卒、宜しくお願い申し上げます。

イメージに合うとても素敵なデザインでした。

この度はまことにありがとうございます。
皆様のご提案に心より感謝申し上げます。
また機会がございましたらよろしくお願い申し上げます。

```html
<!DOCTYPE html>
<html lang="ja">
<head>
<meta charset="utf-8">
<title>梅のさと・ひなたべ のぼり</title>
<link rel="stylesheet" href="https://fonts.googleapis.com/css2?family=Zen+Maru+Gothic:wght@500;700&display=swap">
<style>
  :root {
    --royal-blue: #2d55b8;
    --cloth-white: #f7f8f9;
    --cloth-silver: #e9ebee;
    --backdrop: #d9dbde;
    --art-warm: #f3e6d4;
    --art-green: #e4efdc;
  }
  * { margin: 0; padding: 0; box-sizing: border-box; }
  html, body { width: 675px; height: 1200px; overflow: hidden; }
  body {
    background: var(--backdrop);
    font-family: "Zen Maru Gothic", sans-serif;
    position: relative;
  }
  .nobori {
    position: absolute;
    left: 153px;
    top: 90px;
    width: 369px;
    height: 1069px;
    border: 3px solid var(--royal-blue);
    background: linear-gradient(180deg, var(--cloth-white), var(--cloth-silver));
    display: flex;
    flex-direction: column;
  }
  .mascot-art {
    margin: 10px 14px;
    border-radius: 4px;
    background: linear-gradient(135deg, var(--art-green), var(--cloth-white) 45%, var(--art-warm));
  }
  .mascot-art--top { height: 152px; }
  .mascot-art--bottom { height: 146px; }
  .stripes {
    background: repeating-linear-gradient(180deg,
      var(--royal-blue) 0 18px,
      var(--cloth-white) 18px 34px);
  }
  .stripes--top { height: 248px; }
  .stripes--bottom { height: 338px; }
  .name-band {
    height: 139px;
    background: var(--royal-blue);
    color: var(--cloth-white);
    display: flex;
    flex-direction: column;
    align-items: center;
    justify-content: center;
    gap: 6px;
  }
  .name-band__title {
    font-size: 35px;
    font-weight: 700;
    letter-spacing: 1px;
    line-height: 1;
  }
  .name-band__reading {
    font-size: 15px;
    font-weight: 500;
    letter-spacing: 1.5px;
  }
</style>
</head>
<body>
  <div class="nobori">
    <div class="mascot-art mascot-art--top" role="img" aria-label="親鴨と二羽の子鴨が歩くイラスト"></div>
    <div class="stripes stripes--top"></div>
    <div class="name-band">
      <p class="name-band__title">梅のさと・ひなたべ</p>
      <p class="name-band__reading">ume no sato hinatabe</p>
    </div>
    <div class="stripes stripes--bottom"></div>
    <div class="mascot-art mascot-art--bottom" role="img" aria-label="親鴨と二羽の子鴨が歩くイラスト"></div>
  </div>
</body>
</html>
```